Business card and stationery design

Harbourlight Gatherings Co. is a leading event and conference design and management company.
Please view lumorahostgroup.com.au

The business cards needs to convey:
- professionalism and competency
- exclusivity
- memorable experiences and quality

The business card needs to have the following aspects:
- double sided
- Full colour CMYK
- Printed on either high gloss matt card (designer to recommend)

For the business stationery we require:
- Letterhead with top banner and bottom footer
- A thank you card design
- a with compliments slip design
- a MS powerpoint and MS publisher client presentation slide design which includes cover page and then a standard presentation page
(Note- we do NOT require an envelope design- who sends letters these days!)

The company image is using the key colours of gold, silver and black.
A black background to the business card has been used before and is preferred although we are open to options.

Target Market(s)

High end corporations and businesses that require their events and conferences to be exceptionally well designed and managed

Industry/Entity Type

Business

Contact Information for Business Card

FRONT:

Darian Whitlock
- Event and Conference Specialist

Mobile- +61 (0) 491 238 604
Office- 1300 617 482
dariannw@lumorahostgroup.com.au

Web- lumorahostgroup.com.au

BACK:

- Event and

Font styles to use
Other font styles liked:
• The logo designer used Trajan Pro Bold 3 for the font text in the logo

Requirements
Must have
• Amazing design of the following:
• - business card (double sided)
• - letterhead
• - client thank you card
• - powerpoint and publisher client presentation design files

```html
<!DOCTYPE html>
<html lang="en">
<head>
<meta charset="utf-8">
<title>Harbourlight Gatherings Co. – Business Card</title>
<link href="https://fonts.googleapis.com/css2?family=Montserrat:wght@400;600;700&family=Cinzel:wght@400&display=swap" rel="stylesheet">
<style>
  :root {
    --stage: #e9e6e1;
    --card-black: #0b0b0b;
    --card-sheen: #2a2a2a;
    --gold: #d6b56a;
    --gold-deep: #a8843c;
    --silver: #d9d9d9;
    --panel-olive: #1f231c;
  }
  * { margin: 0; padding: 0; box-sizing: border-box; }
  html, body {
    width: 1200px; height: 913px; overflow: hidden;
    background: var(--stage);
  }
  .canvas {
    position: relative; width: 1200px; height: 913px;
    display: flex; align-items: center; justify-content: center; gap: 48px;
  }
  .card {
    position: relative; width: 532px; height: 304px;
    border-radius: 18px; overflow: hidden;
    background:
      radial-gradient(ellipse 70% 60% at 35% 25%, var(--card-sheen) 0%, transparent 70%),
      var(--card-black);
    box-shadow: 0 14px 30px rgba(0,0,0,.28);
    font-family: "Montserrat", sans-serif;
    color: var(--silver);
  }

  /* Front */
  .front .brand-name {
    position: absolute; left: 34px; top: 118px; width: 170px;
    font-family: "Montserrat", sans-serif; font-weight: 600;
    font-size: 22px; line-height: 1.2; color: var(--gold);
  }
  .front .divider {
    position: absolute; left: 222px; top: 86px; width: 1.5px; height: 132px;
    background: linear-gradient(var(--gold), var(--gold-deep));
  }
  .front .details { position: absolute; left: 244px; top: 84px; }
  .front .person-name {
    font-weight: 700; font-size: 21px; color: var(--gold); letter-spacing: .3px;
  }
  .front .person-role { font-size: 11px; color: var(--silver); margin: 2px 0 12px; }
  .front .contact-list { list-style: none; }
  .front .contact-list li {
    display: flex; align-items: center; gap: 8px;
    font-size: 11.5px; line-height: 20px; color: var(--silver);
  }
  .front .contact-list svg { width: 11px; height: 11px; flex: none; }

  /* Back */
  .back .panel-shape { position: absolute; left: 0; top: 0; }
  .back .brand-name {
    position: absolute; left: 92px; top: 96px; width: 380px;
    font-family: "Montserrat", sans-serif; font-weight: 600;
    font-size: 27px; line-height: 1.15; color: var(--gold);
  }
  .back .rule {
    position: absolute; left: 92px; top: 176px; width: 390px; height: 5px;
    border-top: 2px solid var(--gold); border-bottom: 1px solid var(--silver);
  }
  .back .web {
    position: absolute; right: 40px; bottom: 34px;
    font-family: "Cinzel", serif; font-size: 14px; letter-spacing: 1px;
    color: var(--gold);
  }
</style>
</head>
<body>
<main class="canvas">

  <section class="card front" aria-label="Business card front">
    <div class="brand-name">Harbourlight Gatherings Co.</div>
    <div class="divider"></div>
    <div class="details">
      <p class="person-name">Darian Whitlock</p>
      <p class="person-role">Event and Conference Specialist</p>
      <ul class="contact-list">
        <li>
          <svg viewBox="0 0 12 12" fill="none" stroke="var(--gold)" stroke-width="1.4"><path d="M2.5 1.5 L4.5 1.5 L5.2 4 L4 5 Q5 7.2 7 8 L8 6.8 L10.5 7.5 L10.5 9.5 Q6 10.5 2.5 6 Q1.5 4 2.5 1.5Z"/></svg>
          1300 617 482
        </li>
        <li>
          <svg viewBox="0 0 12 12" fill="none" stroke="var(--gold)" stroke-width="1.4"><rect x="3" y="1" width="6" height="10" rx="1"/><line x1="5.3" y1="9" x2="6.7" y2="9"/></svg>
          +61 (0) 491 238 604
        </li>
        <li>
          <svg viewBox="0 0 12 12" fill="none" stroke="var(--gold)" stroke-width="1.4"><rect x="1" y="2.5" width="10" height="7" rx=".5"/><path d="M1 3 L6 7 L11 3"/></svg>
          dariannw@lumorahostgroup.com.au
        </li>
        <li>
          <svg viewBox="0 0 12 12" fill="none" stroke="var(--gold)" stroke-width="1.2"><circle cx="6" cy="6" r="5"/><ellipse cx="6" cy="6" rx="2.2" ry="5"/><line x1="1" y1="6" x2="11" y2="6"/></svg>
          www.lumorahostgroup.com.au
        </li>
      </ul>
    </div>
  </section>

  <section class="card back" aria-label="Business card back">
    <svg class="panel-shape" width="532" height="304" viewBox="0 0 532 304" aria-hidden="true">
      <polygon points="150,60 400,40 450,120 410,210 120,230 90,150" fill="var(--panel-olive)" opacity=".8"/>
    </svg>
    <div class="brand-name">Harbourlight Gatherings Co.</div>
    <div class="rule"></div>
    <p class="web">WWW.LUMORAHOSTGROUP.COM.AU</p>
  </section>

</main>
</body>
</html>
```